Security Camera Sign

14” high x 11” wide Color: Blue, Yellow, Black and white

Make the sign vertical
Replace red with blue
WARNING: Black over yellow
These premises are protected by Closed Circuit Television: On white
Images are recorded for crime prevention and public safety. Unauthorized access, theft or vandalism will result in prosecution: On Blue

Target Market(s)

Outdoor commercial building

Industry/Entity Type

Security

Requirements
Nice to have
• I would like the sign stand out. If you need more colors? Thanks Ok

```html
<!DOCTYPE html>
<html lang="en">
<head>
<meta charset="utf-8">
<title>Surveillance Sign</title>
<link rel="stylesheet" href="https://fonts.googleapis.com/css2?family=Mulish:wght@800;900&display=swap">
<style>
  :root {
    --page: #ffffff;
    --sign-blue: #1f56b3;
    --sign-blue-deep: #16449a;
    --warning-yellow: #ffe500;
    --ink: #0a0a0a;
    --paper: #ffffff;
    --camera-light: #e9ecef;
    --camera-mid: #b9bfc6;
  }
  html, body {
    margin: 0;
    padding: 0;
    width: 900px;
    height: 1200px;
    overflow: hidden;
    background: var(--page);
  }
  .canvas {
    position: relative;
    width: 900px;
    height: 1200px;
  }
  .sign {
    position: absolute;
    left: 59px;
    top: 97px;
    width: 785px;
    height: 998px;
    box-sizing: border-box;
    border: 3px solid var(--ink);
    border-radius: 4px;
    overflow: hidden;
    background: radial-gradient(ellipse at 50% 48%, var(--sign-blue) 55%, var(--sign-blue-deep) 100%);
    font-family: "Mulish", "Arial", sans-serif;
  }
  .white-band {
    position: absolute;
    left: 0;
    top: 0;
    width: 100%;
    height: 100%;
  }
  .title-plate {
    position: absolute;
    left: 24px;
    top: 70px;
    width: 719px;
    height: 106px;
    box-sizing: border-box;
    background: var(--warning-yellow);
    border: 4px solid var(--ink);
    border-radius: 12px;
    display: flex;
    align-items: center;
    justify-content: center;
  }
  .title {
    margin: 0;
    font-size: 84px;
    font-weight: 900;
    letter-spacing: 1px;
    color: var(--ink);
    line-height: 1;
  }
  .camera-art {
    position: absolute;
    left: 398px;
    top: 207px;
    width: 316px;
    height: 378px;
    border-radius: 40px 40px 60px 40px;
    background: radial-gradient(ellipse at 45% 35%, var(--camera-light) 30%, var(--camera-mid) 100%);
  }
  .cctv-notice {
    position: absolute;
    left: 21px;
    top: 327px;
    width: 460px;
    margin: 0;
    text-align: center;
    font-size: 37px;
    font-weight: 800;
    line-height: 69px;
    color: var(--ink);
  }
  .cctv-notice span { display: block; }
  .legal-notice {
    position: absolute;
    left: 0;
    top: 772px;
    width: 100%;
    margin: 0;
    text-align: center;
    font-size: 33px;
    font-weight: 800;
    line-height: 47.5px;
    color: var(--paper);
  }
  .legal-notice span { display: block; }
</style>
</head>
<body>
<div class="canvas">
  <div class="sign">
    <svg class="white-band" viewBox="0 0 779 992" preserveAspectRatio="none" aria-hidden="true">
      <path d="M0 332 Q390 170 779 332 L779 650 Q390 822 0 650 Z" fill="var(--paper)"/>
    </svg>

    <div class="title-plate">
      <h1 class="title">SURVEILLANCE</h1>
    </div>

    <div class="camera-art" role="img" aria-label="White wall-mounted CCTV security camera on a bracket"></div>

    <p class="cctv-notice">
      <span>THESE</span>
      <span>PREMISES ARE</span>
      <span>PROTECTED</span>
      <span>BY CLOSED</span>
      <span>CIRCUIT TELEVISION</span>
    </p>

    <p class="legal-notice">
      <span>IMAGES ARE RECORDED FOR</span>
      <span>CRIME PREVENTION AND PUBLIC SAFETY.</span>
      <span>UNAUTHORIZED ACCESS, THEFT OR</span>
      <span>VANDALISM WILL RESULT IN PROSECUTION</span>
    </p>
  </div>
</div>
</body>
</html>
```